Business Card and Letterhead Design for Public Accounting Firm

Business card and letterhead design for a CPA Firm located in Orange County, CA. We're looking for a modern and professional design utilizing our existing logo. We'd like a clean "less is more" look, but also something that catches the eye. We provide a high level of service to our clients. Open to single or double sided business cards.

Additional info: color numbers on logo
Blue :
R 0
G 83
B 125

#00537D

Silver :

R 154
G 154
B 154

#9A9A9A

Target Market(s)

Businesses and individuals

Industry/Entity Type

Accounting

Contact Information for Business Card

Moss Whitfield & Danby LLP - 4827 Larkspur Vale Road, Irvine, CA 92614 - (949)731-2864 - mwdaccts.example

Font styles to use
Serif
Sans Serif
Other font styles liked:
• See font file uploaded

Colors
0054AA
0677BA
7BADD7
CADEEF
E8F1F8

Requirements
Nice to have
• Possibly use the font file provided which matches our logo, but adjust to be not in all caps

```html
<!DOCTYPE html>
<html lang="en">
<head>
<meta charset="utf-8">
<title>Moss Whitfield &amp; Danby LLP — Stationery</title>
<link rel="stylesheet" href="https://fonts.googleapis.com/css2?family=Lato:wght@400;700&family=Cormorant+Garamond:wght@500&display=swap">
<style>
  :root {
    --brand-blue: #00537d;
    --brand-silver: #9a9a9a;
    --ink: #1e1e1e;
    --paper: #ffffff;
    --backdrop: #ffffff;
    --edge: #dcdcdc;
  }
  * { box-sizing: border-box; margin: 0; padding: 0; }
  html, body { width: 1200px; height: 807px; overflow: hidden; background: var(--backdrop); }
  body { position: relative; font-family: "Lato", sans-serif; color: var(--ink); }

  .sheet { position: absolute; background: var(--paper); border: 1px solid var(--edge); }
  .wordmark { position: absolute; font-family: "Lato", sans-serif; font-weight: 700; color: var(--brand-blue); white-space: nowrap; display: flex; align-items: center; gap: 6px; }
  .wordmark .dot { display: inline-block; flex: none; background: var(--brand-blue); }
  .wordmark .lines { display: block; line-height: 1.15; }
  .rule { position: absolute; width: 1px; background: var(--brand-blue); }
  .contact { position: absolute; line-height: 1.28; white-space: nowrap; }
  .contact .firm { color: var(--brand-blue); font-weight: 700; }
  .contact .icon { display: inline-block; width: 0.8em; height: 0.8em; vertical-align: -0.05em; margin-right: 0.2em; }

  /* Letterhead */
  .letterhead { left: 136px; top: 97px; width: 431px; height: 610px; }
  .letterhead .wordmark { left: 21px; top: 44px; font-size: 14px; }
  .letterhead .wordmark .dot { width: 10px; height: 10px; }
  .letterhead .rule { left: 286px; top: 28px; height: 68px; }
  .letterhead .contact { left: 312px; top: 27px; font-size: 8.2px; }
  .letterhead .contact .gap { height: 9px; }
  .letter { position: absolute; left: 21px; top: 139px; width: 388px; font-size: 8.8px; line-height: 1.18; }
  .letter p { margin-bottom: 10px; }
  .letter .body p { text-align: justify; margin-bottom: 9.5px; line-height: 1.1; }
  .letter .salutation { font-size: 11px; font-weight: 700; margin-bottom: 12px; }
  .letter .signoff { margin-top: 17px; }
  .signature { width: 92px; height: 22px; margin-top: 40px; background: linear-gradient(90deg, #e9e9e9, #f5f5f5); }

  /* Business cards */
  .card { top: 97px; width: 207px; height: 118px; border-radius: 5px; }
  .card-front { left: 629px; }
  .card-front .wordmark { left: 18px; top: 48px; font-size: 7.6px; gap: 5px; }
  .card-front .wordmark .dot { width: 6px; height: 6px; }
  .card-front .rule { left: 114px; top: 23px; height: 70px; }
  .card-front .person { position: absolute; left: 123px; top: 21px; white-space: nowrap; }
  .card-front .person .name { font-family: "Cormorant Garamond", serif; font-weight: 500; color: var(--brand-blue); font-size: 9px; letter-spacing: 0.05em; line-height: 1.1; }
  .card-front .person .role { font-size: 5.2px; margin-top: 1px; line-height: 1.2; }
  .card-front .contact { left: 123px; top: 46px; font-size: 5px; }
  .card-front .contact .gap { height: 5px; }
  .card-back { left: 852px; background: var(--brand-blue); border-color: var(--brand-blue); }
  .card-back .wordmark { left: 22px; top: 48px; font-size: 11.5px; color: #fff; }
  .card-back .wordmark .dot { width: 9px; height: 9px; background: #fff; }

  /* Envelopes */
  .envelope-back { left: 620px; top: 270px; width: 440px; height: 193px; overflow: hidden; }
  .envelope-back svg { position: absolute; left: 0; top: 0; }
  .envelope-back .wordmark { left: 0; width: 100%; justify-content: center; top: 18px; font-size: 20px; }
  .envelope-back .wordmark .dot { width: 14px; height: 14px; }
  .envelope-front { left: 620px; top: 517px; width: 440px; height: 190px; }
  .envelope-front .wordmark { left: 14px; top: 34px; font-size: 12.5px; }
  .envelope-front .wordmark .dot { width: 9px; height: 9px; }
  .envelope-front .rule { left: 178px; top: 20px; height: 31px; }
  .envelope-front .contact { left: 186px; top: 23px; font-size: 6.2px; }
</style>
</head>
<body>

  <section class="sheet letterhead" aria-label="Letterhead">
    <div class="wordmark"><span class="dot"></span>Moss Whitfield &amp; Danby LLP</div>
    <div class="rule"></div>
    <div class="contact">
      <div><svg class="icon" viewBox="0 0 10 10"><rect x="2.5" y="0.5" width="5" height="9" rx="1" fill="none" stroke="#00537d" stroke-width="1.2"/></svg>(949)731-2864</div>
      <div><svg class="icon" viewBox="0 0 10 10"><rect x="0.5" y="2" width="9" height="6" fill="#00537d"/><path d="M0.5 2 L5 5.5 L9.5 2" stroke="#fff" fill="none"/></svg>cpas@mwdaccts.example</div>
      <div><svg class="icon" viewBox="0 0 10 10"><circle cx="5" cy="5" r="4.5" fill="#00537d"/></svg>www.mwdaccts.example</div>
      <div class="gap"></div>
      <div class="firm">Moss Whitfield &amp; Danby LLP</div>
      <div>4827 Larkspur Vale Road</div>
      <div>Irvine, CA 92614</div>
    </div>

    <div class="letter">
      <p>January-03-2020</p>
      <p>Mr, Paul Garner<br>President</p>
      <p>Fenwick Corporation<br>123 Street Name, Suite# 10<br>City, State, 120023</p>
      <p class="salutation">Dear Mr, Paul</p>
      <div class="body">
        <p>Lorem ipsum dolor sit amet, consectetur adipiscing elit, sed do eiusmod tempor incididunt ut labore et dolore magna aliqua. Ut enim ad minim veniam, quis nostrud exercitation ullamco laboris nisi ut aliquip ex ea commodo consequat. Duis aute irure dolor in reprehenderit in voluptate velit esse cillum dolore eu fugiat nulla pariatur.</p>
        <p>Lorem ipsum dolor sit amet, consectetur adipiscing elit, sed do eiusmod tempor incididunt ut labore et dolore magna aliqua. Ut enim ad minim veniam, quis nostrud exercitation ullamco laboris nisi ut aliquip ex ea commodo consequat. Duis aute irure dolor in reprehenderit in voluptate velit esse cillum dolore eu fugiat nulla pariatur.</p>
        <p>Lorem ipsum dolor sit amet, consectetur adipiscing elit, sed do eiusmod tempor incididunt ut labore et dolore magna aliqua. Ut enim ad minim veniam, quis nostrud exercitation ullamco laboris nisi ut aliquip ex ea commodo consequat.</p>
        <p>Excepteur sint occaecat cupidatat non proident, sunt in culpa qui officia deserunt mollit anim id est laborum. re et dolore magnam aliquam quaerat voluptatem.</p>
      </div>
      <p class="signoff">Regards</p>
      <div class="signature" role="img" aria-label="Handwritten signature of Clara Benton"></div>
    </div>
  </section>

  <section class="sheet card card-front" aria-label="Business card front">
    <div class="wordmark"><span class="dot"></span><span class="lines">Moss Whitfield<br>&amp; Danby LLP</span></div>
    <div class="rule"></div>
    <div class="person">
      <div class="name">OWEN HARTLEY</div>
      <div class="role">Managing Director</div>
    </div>
    <div class="contact">
      <div>(949)731-2864</div>
      <div>cpas@mwdaccts.example</div>
      <div>www.mwdaccts.example</div>
      <div class="gap"></div>
      <div class="firm">Moss Whitfield &amp; Danby LLP</div>
      <div>4827 Larkspur Vale Road</div>
      <div>Irvine, CA 92614</div>
    </div>
  </section>

  <section class="sheet card card-back" aria-label="Business card back">
    <div class="wordmark"><span class="dot"></span>Moss Whitfield &amp; Danby LLP</div>
  </section>

  <section class="sheet envelope-back" aria-label="Envelope back">
    <svg width="440" height="193" viewBox="0 0 440 193" aria-hidden="true">
      <path d="M0.5 0 V30 Q0.5 57 30 57 H410 Q439.5 57 439.5 30 V0" fill="none" stroke="#dcdcdc" stroke-width="1"/>
    </svg>
    <div class="wordmark"><span class="dot"></span>Moss Whitfield &amp; Danby</div>
  </section>

  <section class="sheet envelope-front" aria-label="Envelope front">
    <div class="wordmark"><span class="dot"></span>Moss Whitfield &amp; Danby</div>
    <div class="rule"></div>
    <div class="contact">
      <div class="firm">Moss Whitfield &amp; Danby LLP</div>
      <div>4827 Larkspur Vale Road</div>
      <div>Irvine, CA 92614</div>
    </div>
  </section>

</body>
</html>
```